Banner Ad

We need a banner ad for a service. The service is called, "PipeRook" It compiles tweets and Chatterloom posts about state government issues that are posted by U.S. State Legislators. We have a word cloud containing the issues we want to highlight. And we a logo for PipeRook.

The tag is:
Question: Who Is Talking About Issues on Social Media?
Answer: State Legislators
Are you Listening?

The banner ad will be used for print and web. It will go into a regular weekly publication called The Regional Ledger Roundup. http://www.civicpanel-example.com/the-regional-ledger-roundup/

Industry/Entity Type

Government

```html
<!DOCTYPE html>
<html lang="en">
<head>
<meta charset="utf-8">
<title>PipeRook Banner Ad</title>
<link rel="stylesheet" href="https://fonts.googleapis.com/css2?family=Bebas+Neue&family=Dosis:wght@300;400&display=swap">
<style>
  :root {
    --capitol-blue-deep: #0d3f85;
    --capitol-blue: #1d5fae;
    --capitol-blue-light: #3f7fc4;
    --headline-white: #ffffff;
    --alert-red: #e3202a;
    --cloud-grey: rgba(214, 222, 234, 0.78);
    --skin-tone: #e8b08c;
    --device-dark: #1e1f22;
  }
  * { margin: 0; padding: 0; box-sizing: border-box; }
  html, body { width: 1200px; height: 743px; overflow: hidden; background: #ffffff; }
  .banner {
    position: relative;
    width: 1200px;
    height: 743px;
    overflow: hidden;
    font-family: "Bebas Neue", "Arial Narrow", sans-serif;
  }
  .backdrop {
    position: absolute;
    inset: 0;
    background:
      radial-gradient(ellipse at 62% 48%, var(--capitol-blue-light) 0%, var(--capitol-blue) 40%, var(--capitol-blue-deep) 100%);
  }
  .headline {
    position: absolute;
    left: 46px;
    top: 22px;
    font-size: 62px;
    line-height: 53px;
    color: var(--headline-white);
    letter-spacing: 0.5px;
  }
  .headline .question { color: var(--alert-red); display: block; }
  .headline span { display: block; }
  .device-photo {
    position: absolute;
    left: 0;
    top: 270px;
    width: 415px;
    height: 375px;
    background: linear-gradient(100deg, var(--skin-tone) 0%, var(--skin-tone) 18%, var(--device-dark) 26%, var(--device-dark) 100%);
    border-radius: 0 40px 40px 0;
  }
  .brand {
    position: absolute;
    left: 86px;
    top: 371px;
    width: 272px;
    height: 179px;
    display: flex;
    align-items: center;
    justify-content: center;
    gap: 12px;
    font-size: 44px;
    color: var(--headline-white);
  }
  .brand-mark {
    width: 22px;
    height: 22px;
    background: var(--alert-red);
  }
  .word-cloud {
    position: absolute;
    inset: 0;
    font-family: "Dosis", "Helvetica Neue", sans-serif;
    font-weight: 300;
    color: var(--cloud-grey);
    line-height: 1;
  }
  .issue { position: absolute; white-space: nowrap; }
  .issue-gmo { left: 1036px; top: 296px; font-size: 60px; }
  .issue-sharing { left: 785px; top: 340px; font-size: 52px; }
  .issue-wage { left: 424px; top: 388px; font-size: 56px; }
  .issue-drones { left: 843px; top: 400px; font-size: 36px; }
  .issue-core { left: 990px; top: 410px; font-size: 26px; }
  .issue-driving { left: 424px; top: 445px; font-size: 56px; }
  .issue-privacy { left: 918px; top: 437px; font-size: 78px; }
  .issue-fracking { left: 430px; top: 503px; font-size: 42px; }
  .issue-ecigs { left: 618px; top: 510px; font-size: 56px; }
  .issue-energy { left: 832px; top: 512px; font-size: 40px; }
  .issue-immigration { left: 988px; top: 558px; font-size: 34px; }
  .issue-transport { left: 588px; top: 565px; font-size: 56px; }
  .issue-tax { left: 1043px; top: 596px; font-size: 23px; }
  .issue-climate { left: 843px; top: 617px; font-size: 50px; }
  .contact-bar {
    position: absolute;
    left: 0;
    bottom: 0;
    width: 1200px;
    height: 49px;
    background: var(--alert-red);
    color: var(--headline-white);
    font-size: 27px;
    line-height: 49px;
    padding-left: 16px;
    letter-spacing: 0.3px;
    white-space: nowrap;
  }
</style>
</head>
<body>
  <div class="banner">
    <div class="backdrop" role="img" aria-label="State capitol building framed by trees, toned in deep blue"></div>

    <div class="word-cloud">
      <span class="issue issue-gmo">GMO</span>
      <span class="issue issue-sharing">SharingEconomy</span>
      <span class="issue issue-wage">MinimumWage</span>
      <span class="issue issue-drones">Drones</span>
      <span class="issue issue-core">CommonCore</span>
      <span class="issue issue-driving">DistractedDriving</span>
      <span class="issue issue-privacy">Privacy</span>
      <span class="issue issue-fracking">Fracking</span>
      <span class="issue issue-ecigs">E-Cigs</span>
      <span class="issue issue-energy">AlternativeEnergy</span>
      <span class="issue issue-immigration">Immigration</span>
      <span class="issue issue-transport">Transportation</span>
      <span class="issue issue-tax">TaxReform</span>
      <span class="issue issue-climate">ClimateChange</span>
    </div>

    <h1 class="headline">
      <span>State Legislators</span>
      <span>Are Talking About</span>
      <span>Issues on Social Media</span>
      <span class="question">Are You Listening?</span>
    </h1>

    <div class="device-photo" role="img" aria-label="Hand holding a smartphone showing the PipeRook app"></div>
    <div class="brand">
      <span class="brand-mark"></span>
      <span class="brand-name">PipeRook</span>
    </div>

    <div class="contact-bar">To learn about Capitolside Partners and PipeRook, contact Dana Whitlow at 555-014-2290 or dw@civicpanel-example.com</div>
  </div>
</body>
</html>
```